Tallowreed Advisory Partners Business Card Design

We have the logo we just need someone to design a modern business card design.

Name: Desmond Munkalt
Phone: 3055550148
Mobile: 9175550193
Web:www.tallowreedadvisory.example
email: dmunkalt@tallowreedadvisory.example
Company: Tallowreed Advisory Partners
Title: CEO

Address: 718 Quillmore Ave, Miami, Florida 33190

Target Market(s)

companies over 100 employees

Industry/Entity Type

Business

```html
<!DOCTYPE html>
<html lang="en">
<head>
<meta charset="utf-8">
<title>Tallowreed Advisory Partners – Business Card</title>
<link href="https://fonts.googleapis.com/css2?family=Arimo:wght@400;700&display=swap" rel="stylesheet">
<style>
  :root {
    --ink: #1c1c1c;
    --muted: #3a3a3a;
    --card-light: #e9e9e9;
    --card-dark: #050505;
    --accent: #0d55d9;
    --page: #d8d4ce;
    --on-dark: #d6d6d6;
  }
  * { box-sizing: border-box; margin: 0; padding: 0; }
  html, body {
    width: 1200px; height: 900px; overflow: hidden;
    background: var(--page);
    font-family: "Arimo", Arial, sans-serif;
  }
  .sheet {
    width: 1200px; height: 900px;
    display: flex; align-items: center; justify-content: center; gap: 40px;
  }
  .card {
    width: 560px; height: 320px;
    position: relative; overflow: hidden;
    box-shadow: 0 10px 28px rgba(0,0,0,.22);
  }
  /* Back */
  .card--back { background: var(--card-dark); }
  .card--back .mark-dot {
    position: absolute; left: 50%; top: 96px;
    width: 86px; height: 86px; margin-left: -43px;
    border-radius: 50%; background: var(--accent);
  }
  .card--back .web {
    position: absolute; left: 0; right: 0; bottom: 52px;
    text-align: center; color: var(--on-dark); font-size: 15px; letter-spacing: .2px;
  }
  .web strong { font-weight: 700; }
  /* Front */
  .card--front { background: var(--card-light); color: var(--ink); }
  .card--front .band {
    position: absolute; left: 0; top: 0; bottom: 0; width: 20px; background: var(--accent);
  }
  .brand {
    position: absolute; right: 34px; top: 34px;
    display: flex; flex-direction: column; align-items: flex-end; gap: 10px;
  }
  .brand-dot { width: 48px; height: 48px; border-radius: 50%; background: var(--accent); margin-right: 70px; }
  .brand-name { font-size: 14px; font-weight: 700; color: var(--ink); letter-spacing: .3px; }
  .person { position: absolute; left: 52px; top: 128px; }
  .person-name { font-size: 23px; font-weight: 400; color: var(--muted); }
  .person-title { font-size: 17px; color: var(--muted); margin-top: 4px; }
  .contact { position: absolute; left: 52px; bottom: 30px; font-size: 15px; line-height: 1.45; color: var(--muted); }
  .contact dt { display: inline-block; width: 22px; color: var(--accent); }
  .contact dd { display: inline; }
  .contact .email { margin-top: 6px; }
  .office {
    position: absolute; right: 34px; top: 150px;
    font-size: 14px; line-height: 1.5; color: var(--muted);
  }
</style>
</head>
<body>
<main class="sheet">
  <section class="card card--back" aria-label="Card back">
    <div class="mark-dot"></div>
    <p class="web">www.<strong>tallowreed</strong>advisory.example</p>
  </section>

  <section class="card card--front" aria-label="Card front">
    <div class="band"></div>
    <div class="brand">
      <div class="brand-dot"></div>
      <p class="brand-name">Tallowreed Advisory Partners</p>
    </div>
    <div class="person">
      <h1 class="person-name">Desmond Munkalt</h1>
      <p class="person-title">CEO</p>
    </div>
    <address class="office" style="font-style:normal">
      718 Quillmore Ave, Miami<br>
      Florida 33190<br>
      <span class="web">www.<strong>tallowreed</strong>advisory.example</span>
    </address>
    <dl class="contact">
      <div><dt>T</dt><dd>3055550148</dd></div>
      <div><dt>M</dt><dd>9175550193</dd></div>
      <div class="email">dmunkalt@tallowreedadvisory.example</div>
    </dl>
  </section>
</main>
</body>
</html>
```